Girls Night Out Flyer for a female oriented event

I need a flyer to promote my event which should look "FUN" and "Sophisticated"
I would need the flyer to be 8 1/2" X 11" 300 dpi. I would need the layered .psd file as well as all the fonts. The flyer should contain the following info:

Velvet Evening Soiree CT
Friday, September 25th
6:00-10:00 PM
The Willow Hall Pavilion
14 Marlow Rd
Danbury, CT 06811
First 100 guests will have a chance to win $25,000 and receive a swag bag filled with gifts
$20 Advanced Admission at www.velveteveningsoireect.com
$25 at the door
(Key words)
Martini Bar
Wine Tasting
Food Sampling
Beauty Make-Overs
Fashion Shows
Psychic Readings
Shopping
Door Prizes
Swag Bag
Exhibitors
For tickets visit www.velveteveningsoireect.com

Target Market(s)

Ladies

Industry/Entity Type

Event

Requirements
Must have
• see description

```html
<!DOCTYPE html>
<html lang="en">
<head>
<meta charset="utf-8">
<title>Velvet Evening Soiree CT</title>
<link rel="stylesheet" href="https://fonts.googleapis.com/css2?family=Yellowtail&family=Dekko&family=Handlee&family=Fredoka:wght@600&family=Varela+Round&display=swap">
<style>
  :root {
    --paper: #ffffff;
    --ink: #111111;
    --green: #5cbf3a;
    --lime-outline: #f2ee2a;
    --sky: #27a9e1;
    --magenta: #ec1c8c;
    --purple: #7d58a8;
    --orange: #f26a2a;
    --gold: #f7c41a;
    --admission: #4fb848;
  }
  * { box-sizing: border-box; margin: 0; padding: 0; }
  html, body { width: 900px; height: 1200px; overflow: hidden; background: var(--paper); }
  .flyer { position: relative; width: 900px; height: 1200px; overflow: hidden; background: var(--paper); color: var(--ink); }
  .flyer > * { position: absolute; white-space: nowrap; }

  .keyword { font-family: "Handlee", cursive; font-size: 23px; color: var(--ink); z-index: 2; }
  .kw-swag { left: 52px; top: 54px; transform: rotate(-3deg); }
  .kw-door { left: 706px; top: 72px; transform: rotate(8deg); }
  .kw-beauty { left: 40px; top: 480px; }
  .kw-exhibitors { left: 730px; top: 594px; }
  .kw-martini { left: 170px; top: 670px; transform: rotate(5deg); }
  .kw-wine { left: 557px; top: 658px; transform: rotate(4deg); }
  .kw-food { left: 386px; top: 897px; transform: rotate(-10deg); }
  .kw-shopping { left: 460px; top: 997px; transform: rotate(4deg); }
  .kw-psychic { left: 694px; top: 1086px; transform: rotate(-5deg); }
  .kw-fashion { left: 76px; top: 1124px; transform: rotate(3deg); }

  .event-title {
    left: 175px; width: 515px; top: 44px; text-align: center;
    font-family: "Yellowtail", cursive; font-weight: 400; font-size: 50px; color: var(--green);
    -webkit-text-stroke: 2px var(--lime-outline); paint-order: stroke fill;
    text-decoration: underline; text-decoration-color: var(--green); text-decoration-thickness: 3px; text-underline-offset: 5px;
    z-index: 2;
  }
  .event-date {
    left: 40px; top: 170px; transform: rotate(-7deg); transform-origin: left top;
    font-family: "Dekko", cursive; font-size: 40px; color: var(--sky);
    text-decoration: underline; text-underline-offset: 3px;
  }
  .event-time {
    left: 132px; top: 208px; transform: rotate(-3deg);
    font-family: "Varela Round", sans-serif; font-size: 36px; color: var(--magenta);
    -webkit-text-stroke: 2px var(--gold); paint-order: stroke fill;
    text-decoration: underline; text-underline-offset: 3px;
  }
  .venue { left: 455px; top: 198px; width: 410px; text-align: center; font-family: "Dekko", cursive; color: var(--purple); font-style: normal; }
  .venue p { text-decoration: underline; text-underline-offset: 3px; line-height: 50px; }
  .venue-name { font-size: 34px; }
  .venue-street { font-family: "Fredoka", sans-serif; font-weight: 600; font-size: 28px; color: var(--gold); -webkit-text-stroke: 1px var(--purple); paint-order: stroke fill; text-decoration-color: var(--purple); }
  .venue-city { font-size: 32px; }

  .giveaway { left: 30px; top: 348px; width: 860px; text-align: center; transform: rotate(3deg); font-family: "Dekko", cursive; font-size: 29px; color: var(--orange); line-height: 54px; }
  .giveaway p { text-decoration: underline; text-underline-offset: 3px; }
  .highlight { font-family: "Fredoka", sans-serif; font-weight: 600; color: var(--gold); -webkit-text-stroke: 1px var(--orange); paint-order: stroke fill; font-size: 29px; }

  .admission { left: 70px; top: 520px; width: 780px; text-align: center; transform: rotate(-5deg); font-family: "Dekko", cursive; font-size: 29px; color: var(--admission); line-height: 50px; }
  .admission p { text-decoration: underline; text-underline-offset: 3px; }
  .admission .price { font-family: "Fredoka", sans-serif; font-weight: 600; color: var(--gold); -webkit-text-stroke: 1px var(--admission); paint-order: stroke fill; font-size: 31px; }

  .party-art {
    left: 20px; top: 690px; width: 870px; height: 490px; border-radius: 24px; z-index: 0;
    background:
      radial-gradient(circle at 15% 18%, rgba(240,230,40,.30), transparent 28%),
      radial-gradient(circle at 40% 28%, rgba(242,106,42,.24), transparent 26%),
      radial-gradient(circle at 65% 14%, rgba(39,169,225,.26), transparent 28%),
      radial-gradient(circle at 90% 22%, rgba(125,88,168,.26), transparent 26%),
      linear-gradient(180deg, rgba(255,255,255,0) 40%, rgba(40,40,40,.12) 100%);
  }

  .tickets { left: 200px; width: 560px; top: 1070px; text-align: center; font-family: "Dekko", cursive; font-size: 23px; color: var(--magenta); line-height: 33px; z-index: 2; }
  .tickets p { text-decoration: underline; }
  .tickets .accent { font-family: "Fredoka", sans-serif; font-weight: 600; color: var(--gold); -webkit-text-stroke: 0.8px var(--magenta); paint-order: stroke fill; font-size: 21px; }
  .event-date, .event-time, .venue, .giveaway, .admission { z-index: 2; }
</style>
</head>
<body>
<main class="flyer">
  <div class="party-art" role="img" aria-label="Colourful starbursts and silhouettes of women dancing"></div>

  <span class="keyword kw-swag">Swag Bag</span>
  <h1 class="event-title">Velvet Evening Soiree CT</h1>
  <span class="keyword kw-door">Door Prizes</span>

  <p class="event-date">Friday, September 25th</p>
  <p class="event-time">6:00-10:00 PM</p>

  <address class="venue">
    <p class="venue-name">The Willow Hall Pavilion</p>
    <p class="venue-street">14 Marlow Rd</p>
    <p class="venue-city">Danbury, CT 06811</p>
  </address>

  <div class="giveaway">
    <p>First <span class="highlight">100</span> guests will have a chance to win <span class="highlight">$25,000</span> and</p>
    <p>receive a <span class="highlight">swag bag filled with gifts</span></p>
  </div>

  <span class="keyword kw-beauty">Beauty Make-Overs</span>

  <div class="admission">
    <p><span class="price">$</span>20 Advanced Admission at www.velveteveningsoireect.com</p>
    <p><span class="price">$</span>25 at the door</p>
  </div>

  <span class="keyword kw-exhibitors">Exhibitors</span>
  <span class="keyword kw-martini">Martini Bar</span>
  <span class="keyword kw-wine">Wine Tasting</span>
  <span class="keyword kw-food">Food Sampling</span>
  <span class="keyword kw-shopping">Shopping</span>
  <span class="keyword kw-psychic">Psychic Readings</span>
  <span class="keyword kw-fashion">Fashion Shows</span>

  <div class="tickets">
    <p>Deadline</p>
    <p>Friday, <span class="accent">June 12</span>, 2015</p>
    <p>For tickets visit <span class="accent">www.velveteveningsoireect.com</span></p>
  </div>
</main>
</body>
</html>
```